Electronic Music Artist needs an Album Cover

DRELL is an electronic musician from Boston, Massachusetts. He needs an album cover that captures the essence of his music. The album is called Lanterns, which represents his experiences growing up, positive and negative. He would like to see designs that involves color and creativity. Attached are some examples of artworks that DRELL likes. He also included a few of his original photos (optional to use. Using a photo will not effect his final decision!), and his logo.

Colors

Designer to choose colors to be used in the design.

Requirements
Must have
• My project must have the text "Lanterns" and "DRELL", and the logo (attached in the files). The logo should not be the main subject of the artwork. Everything must look aesthetically pleasing.
Nice to have
• It would be nice to have some sort of creative graphic design (see example album covers for reference). Also, in one of the references, there is a column on the left hand side with some text in it. That could be cool to include, but without the asian text.
Should not have
• The project should not have any other language besides English.

```html
<!DOCTYPE html>
<html lang="en">
<head>
<meta charset="utf-8">
<title>DRELL – Lanterns</title>
<link rel="stylesheet" href="https://fonts.googleapis.com/css2?family=Oswald:wght@600&family=Rye&display=swap">
<style>
  :root {
    --bg-deep: #1a1512;
    --bg-warm: #2a211b;
    --bg-glow: #4a3a2c;
    --artist-orange: #f2a73e;
    --title-silver: #dfe4ea;
    --title-steel: #9aa3ad;
    --title-shadow: #0b0908;
    --mark-grey: #c4c8cd;
    --sky-blue: #3f86b8;
    --sky-pink: #e8607a;
    --sky-orange: #f08a3c;
    --sky-violet: #4b3f8a;
  }
  html, body {
    margin: 0;
    padding: 0;
    width: 1200px;
    height: 1193px;
    overflow: hidden;
    background: var(--bg-deep);
  }
  .cover {
    position: relative;
    width: 1200px;
    height: 1193px;
    overflow: hidden;
    background:
      radial-gradient(ellipse 70% 12% at 45% 4%, var(--bg-glow), transparent 70%),
      repeating-radial-gradient(circle at 30% 40%, rgba(255,255,255,0.025) 0 3px, transparent 3px 9px),
      linear-gradient(180deg, var(--bg-warm) 0%, var(--bg-deep) 55%, var(--bg-deep) 100%);
  }
  .photo {
    position: absolute;
  }
  .photo--left {
    left: 105px;
    top: 190px;
    width: 355px;
    height: 580px;
    background: linear-gradient(180deg, var(--sky-blue) 0%, #d9d2cf 22%, var(--sky-orange) 55%, var(--sky-pink) 72%, var(--sky-violet) 100%);
    opacity: 0.9;
  }
  .photo--right {
    left: 680px;
    top: 215px;
    width: 485px;
    height: 520px;
    background: linear-gradient(90deg, var(--sky-blue) 0%, var(--sky-pink) 45%, rgba(90,60,90,0.6) 75%, rgba(40,30,35,0.2) 100%);
    opacity: 0.85;
  }
  .artist-name {
    position: absolute;
    left: 546px;
    top: 480px;
    transform: translate(-50%, -50%) rotate(90deg);
    margin: 0;
    font-family: "Oswald", sans-serif;
    font-weight: 600;
    font-size: 150px;
    line-height: 1;
    letter-spacing: 4px;
    color: var(--artist-orange);
    white-space: nowrap;
  }
  .album-title {
    position: absolute;
    left: 600px;
    top: 985px;
    transform: translate(-50%, -50%) rotate(-7deg) skewX(-6deg);
    margin: 0;
    font-family: "Rye", serif;
    font-weight: 400;
    font-size: 150px;
    line-height: 1;
    letter-spacing: 2px;
    white-space: nowrap;
    color: var(--title-silver);
    background: linear-gradient(180deg, #ffffff 0%, var(--title-silver) 45%, var(--title-steel) 100%);
    -webkit-background-clip: text;
    background-clip: text;
    -webkit-text-fill-color: transparent;
    filter: drop-shadow(4px 5px 0 var(--title-shadow));
  }
  .label-mark {
    position: absolute;
    right: 40px;
    bottom: 70px;
    display: flex;
    align-items: center;
    gap: 10px;
    font-family: "Oswald", sans-serif;
    font-weight: 600;
    font-size: 34px;
    line-height: 1;
    color: var(--mark-grey);
  }
  .label-mark__square {
    width: 26px;
    height: 26px;
    background: var(--mark-grey);
  }
</style>
</head>
<body>
  <main class="cover">
    <div class="photo photo--left" role="img" aria-label="Silhouette of a saxophonist playing at an observation deck window against a sunset sky"></div>
    <div class="photo photo--right" role="img" aria-label="City skyline with a lit tower seen through a window at dusk"></div>
    <h1 class="artist-name">DRELL</h1>
    <h2 class="album-title">LANTERNS</h2>
    <div class="label-mark"><span class="label-mark__square"></span><span>DRELL</span></div>
  </main>
</body>
</html>
```